Email Newsletter Banner

I require 2 new email newsletter and web banners to be made up.
I require the brand names to be included on the banner which are " Gadget Dispatch" and "Byte Wirez". I would also like some sort of imagery and also a "sign up here" button. Please see below examples:
https://fernvalepages.lumoshelf.com/
https://brightquarryhub.lumoshelf.com/
https://oakdalereads.lumoshelf.com/

```html
<!DOCTYPE html>
<html lang="en">
<head>
<meta charset="utf-8">
<title>Email Banner Design – Mockup 2</title>
<link rel="stylesheet" href="https://fonts.googleapis.com/css2?family=Exo+2:ital,wght@0,300;0,700;0,800;1,500;1,700;1,800&family=Josefin+Sans:wght@700&display=swap">
<style>
  :root {
    --ink: #111111;
    --accent: #1a9ad6;
    --board-top: #e9e9e8;
    --board-bottom: #f6f6f6;
    --sky-light: #4fd0f5;
    --sky-mid: #1db8ee;
    --sky-deep: #0a9ee0;
    --navy-deep: #0a1a6e;
    --navy-mid: #0d2fa8;
    --cyan-text: #38d8f2;
    --white: #ffffff;
    --gold-light: #fff27a;
    --gold: #f5d80a;
    --gold-deep: #e4b900;
    --amber-light: #f5d45e;
    --amber: #d6a51a;
    --button-ink: #2a2200;
  }
  * { box-sizing: border-box; margin: 0; padding: 0; }
  html, body { width: 1200px; height: 793px; overflow: hidden; }
  body {
    position: relative;
    background: linear-gradient(180deg, var(--board-top), var(--board-bottom));
    font-family: "Exo 2", sans-serif;
  }
  .board-header {
    position: absolute; left: 0; top: 0; width: 1200px; height: 143px;
    background: var(--white);
    text-align: center;
    font-family: "Josefin Sans", sans-serif;
    font-weight: 700;
  }
  .board-title { position: absolute; left: 0; right: 0; top: 31px; font-size: 26px; letter-spacing: 1px; color: var(--ink); }
  .board-subtitle { position: absolute; left: 0; right: 0; top: 69px; font-size: 27px; letter-spacing: 1.2px; color: var(--accent); }

  .banner { position: absolute; height: 96px; overflow: hidden; }
  .banner--small { left: 54px; width: 780px; }
  .banner--large { left: 42px; width: 1039px; }
  .banner--news {
    background:
      radial-gradient(ellipse at 20% 30%, rgba(255,255,255,.25), transparent 55%),
      linear-gradient(90deg, var(--sky-light), var(--sky-mid) 55%, var(--sky-deep));
  }
  .banner--bulletin {
    background:
      radial-gradient(ellipse at 55% 60%, var(--navy-mid), transparent 70%),
      linear-gradient(90deg, var(--navy-deep), #0b2590 50%, var(--navy-deep));
  }

  .brand { position: absolute; top: 0; height: 96px; display: flex; align-items: center; gap: 14px; color: var(--white); white-space: nowrap; }
  .brand-dot { width: 26px; height: 26px; border-radius: 50%; background: rgba(255,255,255,.85); }
  .banner--bulletin .brand-dot { background: #1fb9b0; }
  .brand-name--news { font-weight: 800; }
  .brand-name--bulletin { font-weight: 300; }

  .tagline { position: absolute; top: 0; height: 96px; display: flex; flex-direction: column; justify-content: center; font-style: italic; white-space: nowrap; line-height: 1; }
  .tagline-top { color: var(--white); letter-spacing: 1px; }
  .tagline-top strong { font-weight: 800; }
  .tagline-top span { font-weight: 500; }
  .tagline-bottom { font-weight: 800; letter-spacing: 2px; color: var(--white); text-align: right; }
  .banner--bulletin .tagline-top { font-weight: 800; }
  .banner--bulletin .tagline-bottom { color: var(--cyan-text); letter-spacing: 1px; }

  .signup {
    position: absolute; top: 28px; width: 100px; height: 40px;
    border-radius: 3px; display: flex; align-items: center; justify-content: center;
    font-style: italic; font-weight: 800; font-size: 18px; color: var(--button-ink);
    background: linear-gradient(180deg, var(--gold-light), var(--gold) 50%, var(--gold-deep));
    box-shadow: 0 2px 3px rgba(0,0,0,.2);
  }
  .signup--gold {
    background: linear-gradient(180deg, var(--amber-light), var(--amber));
    color: var(--white);
    text-shadow: 0 1px 1px rgba(0,0,0,.5);
  }
</style>
</head>
<body>
  <header class="board-header">
    <h1 class="board-title">EMAILBANNER DESIGN - MOCKUP 2</h1>
    <p class="board-subtitle">2 DESIGN- 2MOCK UPS - 2 DIFFERENT SIZES</p>
  </header>

  <!-- Small size -->
  <section class="banner banner--small banner--news" style="top:196px">
    <div class="brand" style="left:30px"><span class="brand-dot"></span><span class="brand-name--news" style="font-size:38px">Byte Wirez</span></div>
    <div class="tagline" style="left:300px">
      <p class="tagline-top" style="font-size:20px"><strong>DELIVERING</strong> <span>THE LATEST IT NEWS</span></p>
      <p class="tagline-bottom" style="font-size:31px">TO YOUR INBOX</p>
    </div>
    <a class="signup" style="left:665px">SIGN UP</a>
  </section>

  <section class="banner banner--small banner--bulletin" style="top:311px">
    <div class="brand" style="left:30px"><span class="brand-dot"></span><span class="brand-name--bulletin" style="font-size:30px">Gadget Dispatch</span></div>
    <div class="tagline" style="left:300px">
      <p class="tagline-top" style="font-size:20px">ESSENTIAL WHITEPAPERS FOR</p>
      <p class="tagline-bottom" style="font-size:29px">IT Professionals</p>
    </div>
    <a class="signup signup--gold" style="left:663px">SIGN UP</a>
  </section>

  <!-- Large size -->
  <section class="banner banner--large banner--news" style="top:471px">
    <div class="brand" style="left:50px"><span class="brand-dot" style="width:32px;height:32px"></span><span class="brand-name--news" style="font-size:50px">Byte Wirez</span></div>
    <div class="tagline" style="left:402px">
      <p class="tagline-top" style="font-size:25px"><strong>DELIVERING</strong> <span>THE LATEST IT NEWS</span></p>
      <p class="tagline-bottom" style="font-size:39px">TO YOUR INBOX</p>
    </div>
    <a class="signup" style="left:889px">SIGN UP</a>
  </section>

  <section class="banner banner--large banner--bulletin" style="top:586px">
    <div class="brand" style="left:42px"><span class="brand-dot"></span><span class="brand-name--bulletin" style="font-size:30px">Gadget Dispatch</span></div>
    <div class="tagline" style="left:354px">
      <p class="tagline-top" style="font-size:21px">ESSENTIAL WHITEPAPERS FOR</p>
      <p class="tagline-bottom" style="font-size:34px;margin-right:-70px">IT Professionals</p>
    </div>
    <a class="signup signup--gold" style="left:889px">SIGN UP</a>
  </section>
</body>
</html>
```